Chimney Service company needs new business card design

We need a updated business card with our new logo added. We provide a full range of chimney services throughout Vermont and New Hampshire. The business card will be one sided and color. Attached is our current business card another document showing all the information we would like on the card.
We dont like a lot of flashy colors.... here is a link to our website to get an idea of our branding www.flueguardianvt.example

Target Market(s)

homeowners

Industry/Entity Type

Business

Contact Information for Business Card

See attached sheet for content.

Font styles to use
Serif
Sans Serif

Requirements
Must have
• all information provided on separate sheet
Should not have
• Additional information that may clogg up design

```html
<!DOCTYPE html>
<html lang="en">
<head>
<meta charset="utf-8">
<title>Flue Guardian – Business Card</title>
<link rel="stylesheet" href="https://fonts.googleapis.com/css2?family=Cinzel:wght@600&family=Mulish:ital,wght@1,500&family=Arimo:wght@400;700&display=swap">
<style>
  :root {
    --bg: #e9ebec;
    --card: #ffffff;
    --red: #c8143c;
    --charcoal: #2a2a2c;
    --ink: #1d1d1f;
    --mark-grey: #dcdcdc;
  }
  html, body {
    margin: 0;
    width: 1200px;
    height: 900px;
    overflow: hidden;
    background: var(--bg);
  }
  .card {
    position: absolute;
    left: 100px;
    top: 160px;
    width: 1000px;
    height: 580px;
    background: var(--card);
    box-shadow: 0 10px 30px rgba(0,0,0,.18);
    overflow: hidden;
  }
  .band-top {
    position: absolute; left: 0; right: 0; top: 0;
    height: 6px; background: var(--red);
    border-bottom: 3px solid var(--charcoal);
  }
  .band-bottom {
    position: absolute; left: 0; right: 0; bottom: 0;
    height: 12px; background: var(--charcoal);
    border-bottom: 7px solid var(--red);
  }
  .brand-backdrop {
    position: absolute;
    right: 24px; top: 150px;
    width: 250px; height: 380px;
    background: var(--mark-grey);
    opacity: .7;
  }
  .brand {
    position: absolute;
    left: 64px; top: 48px;
    display: flex; align-items: center; gap: 18px;
  }
  .brand-square {
    width: 58px; height: 58px;
    background: var(--charcoal);
  }
  .brand-name {
    font-family: "Cinzel", serif;
    font-weight: 600;
    font-size: 38px;
    letter-spacing: 1px;
    color: var(--charcoal);
  }
  .services {
    position: absolute;
    left: 50px; top: 140px;
    margin: 0; padding: 0 0 0 22px;
    font-family: "Mulish", sans-serif;
    font-style: italic;
    font-weight: 500;
    font-size: 24px;
    line-height: 36px;
    color: var(--red);
  }
  .services li::marker { color: var(--ink); }
  .details {
    position: absolute;
    left: 420px; top: 130px;
    width: 390px;
    text-align: center;
    font-family: "Arimo", sans-serif;
    font-weight: 700;
    font-size: 25px;
    line-height: 32px;
    color: var(--ink);
  }
  .details p { margin: 0; }
  .contact {
    position: absolute;
    left: 440px; top: 302px;
    font-family: "Arimo", sans-serif;
    font-size: 26px;
    color: var(--ink);
  }
  .contact-label { margin: 0 0 6px 14px; }
  .contact ul { margin: 0; padding: 0 0 0 26px; line-height: 36px; }
  .contact li { color: var(--red); font-size: 28px; }
  .contact li::marker { color: var(--ink); }
</style>
</head>
<body>
  <div class="card">
    <div class="band-top"></div>
    <div class="brand-backdrop" role="img" aria-label="Faint brand backdrop panel"></div>

    <div class="brand">
      <div class="brand-square"></div>
      <div class="brand-name">FLUE GUARDIAN</div>
    </div>

    <ul class="services">
      <li>Full Masonry Services</li>
      <li>Historic Chimney Restoration</li>
      <li>Stainless Steel Liners</li>
      <li>New Chimney Installations</li>
      <li>CSIA Certified Chimney Sweeps</li>
      <li>Fully Insured – Free Estimates</li>
      <li>Family Owned And Aperated</li>
    </ul>

    <div class="details">
      <p>Serving VT &amp; NewHampshire</p>
      <p>Since 1989</p>
      <p>802-555-0147</p>
    </div>

    <div class="contact">
      <p class="contact-label">Contact:</p>
      <ul>
        <li>info@flueguardianvt.example</li>
        <li>www.flueguardianvt.example</li>
      </ul>
    </div>

    <div class="band-bottom"></div>
  </div>
</body>
</html>
```